Clara Joy Halden- Lantern Waltz- Autumn/Winter Tour Dates

I need high res A3 Tour poster for print and for social media JPG sharing of tour dates.
Also needed Kith/Twitter Banner Cover Photos of these dates.
Text Needed Below
Clara Joy Halden
Lantern Waltz
Autumn/Winter Tour Dates
03/09 Ravensby Folk Festival
21/09 Swindon- Calder Theatre
01/10 Hitchin- Brackwell Folk Club
17/10 Bath- The Anvil
20/10 Sheffield- Upper Dale Croquet Club
24/10 Birmingham- Orchard Lamp Cafe
26/10 Glasgow- The Nook and Jar
27/10 Edinburgh - The Marble Parlour
08/11 Capital Reel and Ballad Festival- The Crooked Heron
25/11 Lewes- Tandem Record Shop- Live In Store
02/12 Cambridge- The Quayside
27/01 Lincolnshire- Fenmarsh Theatre
Tickets/Info: www.clarajoyhalden-music.example/gigs
(Quotes/Reviews To Put On)
"Outstanding, rich and expressive."            "Vibrant and Experimental"
**** BdM                                                               **** Tunepaths
"Impressive and Invigorating"                        "Enchanting" Acoustic Wire UK
tBarks

Updates
I cannot read the tour dates on most of the submissions so far. They need to be visible to viewers.
Thank You.
Please also be as creative and inventive as possible- not bland.

Target Market(s)
Music Fans- Folk Acoustic Americana
Industry/Entity Type
Media
Font styles to use
Requirements
Must have
- My photo featured prominently
- Look classy and not tacky or OTT
- Look elegant, wintery and eye catching
- The dates must be very clear to read
- Links to Website:

Nice to have
- Something innovative and not boring in terms of layout design
- Perhaps fading/ misty or wintery

Should not have
- Any colours that do not match

```html
<!DOCTYPE html>
<html lang="en">
<head>
<meta charset="utf-8">
<title>Clara Joy Halden – Lantern Waltz – Artist Page with Tour Cover</title>
<link rel="stylesheet" href="https://fonts.googleapis.com/css2?family=Arimo:wght@400;700&family=Parisienne&family=Cormorant+Garamond:ital,wght@0,500;0,600;0,700;1,500;1,600&display=swap">
<style>
  :root {
    --white: #ffffff;
    --page: #e9ebee;
    --bar: #3b5998;
    --action: #4267b2;
    --link: #365899;
    --text: #1d2129;
    --muted: #90949c;
    --body: #4b4f56;
    --line: #dddfe2;
    --btn-bg: #f6f7f9;
    --btn-line: #ced0d4;
    --green: #42b72a;
    --event-red: #e0393e;
    --ink: #f2f1eb;
    --ink-soft: #d4d8d2;
    --mist-dark: #1f2a28;
    --mist-mid: #43524d;
    --mist-light: #9aa59f;
  }
  * { margin: 0; padding: 0; box-sizing: border-box; }
  html, body { width: 1200px; height: 1000px; overflow: hidden; background: var(--white); }
  body { position: relative; font-family: "Arimo", Arial, sans-serif; color: var(--text); }
  .abs { position: absolute; }

  /* page frame */
  .page { position: absolute; left: 65px; top: 35px; width: 1065px; height: 903px; background: var(--page); overflow: hidden; }
  .topbar { position: absolute; left: 65px; top: 35px; width: 1065px; height: 42px; background: var(--bar); }
  .topbar__brand { position: absolute; left: 27px; top: 13px; color: var(--white); font-weight: 700; font-size: 15px; }
  .topbar__search { position: absolute; left: 58px; top: 8px; width: 446px; height: 24px; background: var(--white); border-radius: 2px; }
  .topbar__search-btn { position: absolute; left: 458px; top: 8px; width: 46px; height: 24px; background: var(--btn-bg); border-left: 1px solid var(--line); border-radius: 0 2px 2px 0; }
  .topbar__divider { position: absolute; top: 10px; width: 1px; height: 22px; background: rgba(0,0,0,0.25); }
  .topbar__home { position: absolute; left: 809px; top: 14px; color: var(--white); font-weight: 700; font-size: 12px; }
  .topbar svg { position: absolute; }

  /* left column */
  .profile-pic { position: absolute; left: 91px; top: 90px; width: 180px; height: 180px; background: var(--white); border: 1px solid var(--line); padding: 4px; }
  .profile-pic__art { width: 100%; height: 100%; background: radial-gradient(circle at 50% 45%, #3f6a8e, #142a44 70%, #0c1a2d); }
  .profile-name { position: absolute; left: 91px; top: 286px; font-size: 19px; color: var(--text); }
  .profile-handle { position: absolute; left: 91px; top: 313px; font-size: 14px; font-weight: 700; color: var(--muted); }
  .side-nav { position: absolute; left: 87px; top: 345px; width: 184px; list-style: none; }
  .side-nav li { height: 32px; line-height: 28px; padding-left: 8px; font-size: 14px; color: var(--text); }
  .side-nav .is-active { background: #f5f6f7; border: 1px solid var(--line); border-radius: 2px; font-weight: 700; padding-left: 7px; height: 29px; margin-bottom: 3px; }
  .create-page { position: absolute; left: 91px; top: 678px; width: 99px; height: 23px; background: var(--green); color: var(--white); border-radius: 2px; font-size: 12px; font-weight: 700; text-align: center; line-height: 23px; }

  /* cover */
  .cover { position: absolute; left: 283px; top: 77px; width: 820px; height: 311px; overflow: hidden; color: var(--ink); font-family: "Cormorant Garamond", Georgia, serif; }
  .cover__photo { position: absolute; inset: 0;
    background:
      radial-gradient(ellipse 200px 200px at 580px 130px, rgba(175,184,178,0.6), transparent 70%),
      radial-gradient(ellipse 300px 220px at 170px 300px, rgba(18,26,25,0.65), transparent 70%),
      linear-gradient(100deg, var(--mist-dark) 0%, var(--mist-mid) 45%, var(--mist-light) 72%, var(--mist-mid) 100%); }
  .cover__frame { position: absolute; inset: 0; }
  .cover__col { position: absolute; left: 0; width: 530px; text-align: center; white-space: nowrap; }
  .cover__title { top: 1px; font-family: "Parisienne", cursive; font-weight: 400; font-size: 37px; line-height: 44px; }
  .cover__subtitle { top: 41px; font-size: 11px; line-height: 14px; letter-spacing: 3.2px; font-weight: 500; }
  .cover__season { top: 61px; font-style: italic; font-size: 16px; line-height: 18px; letter-spacing: 1px; font-weight: 500; }
  .tour-dates { top: 81px; list-style: none; }
  .tour-dates li { height: 16px; line-height: 16px; font-size: 13.5px; letter-spacing: 0.4px; }
  .tour-dates .date { font-style: italic; font-weight: 500; }
  .tour-dates .date sup { font-size: 8px; vertical-align: 5px; }
  .tour-dates .city { font-weight: 700; text-transform: uppercase; margin-left: 5px; }
  .tour-dates .venue { font-style: italic; font-weight: 600; margin-left: 4px; }
  .cover__tickets { top: 276px; font-size: 11px; line-height: 18px; letter-spacing: 1.2px; }
  .cover__tickets .url { font-style: italic; font-weight: 600; font-size: 14.5px; letter-spacing: 0.8px; margin-left: 3px; }
  .review { position: absolute; text-align: right; white-space: nowrap; }
  .review__quote { font-style: italic; font-weight: 500; font-size: 21.5px; line-height: 22px; letter-spacing: 0.8px; }
  .review__source { font-size: 8px; letter-spacing: 1px; color: var(--ink-soft); }

  /* action bar */
  .actions { position: absolute; left: 283px; top: 388px; width: 820px; height: 53px; background: var(--white); border-bottom: 1px solid var(--line); }
  .btn-group { position: absolute; left: 12px; top: 13px; height: 27px; display: flex; border: 1px solid var(--btn-line); border-radius: 2px; background: var(--btn-bg); }
  .btn-group span { display: flex; align-items: center; gap: 5px; padding: 0 10px; font-size: 12px; font-weight: 700; color: var(--body); border-right: 1px solid var(--btn-line); }
  .btn-group span:last-child { border-right: 0; }
  .send-btn { position: absolute; left: 520px; top: 13px; width: 288px; height: 27px; background: var(--action); color: var(--white); border-radius: 2px; font-size: 13px; font-weight: 700; text-align: center; line-height: 27px; }

  /* cards */
  .card { position: absolute; background: var(--white); border: 1px solid #dddfe2; border-radius: 3px; overflow: hidden; }
  .card__title { position: absolute; left: 12px; font-size: 14px; font-weight: 700; color: var(--text); }
  .card__label { position: absolute; left: 12px; font-size: 11px; font-weight: 700; color: var(--text); }
  .close-box { position: absolute; width: 15px; height: 15px; background: #bec2c9; }
  .close-box svg { display: block; }

  .featured { left: 283px; top: 455px; width: 501px; height: 268px; }
  .review-clip { position: absolute; left: 7px; top: 42px; width: 286px; height: 216px; border: 1px solid var(--line); }
  .review-clip__text { position: absolute; left: 25px; top: 4px; width: 244px; height: 155px; overflow: hidden; font-size: 10.4px; line-height: 15.2px; color: #333; text-align: justify; }
  .review-clip__text p + p { margin-top: 0; }
  .review-clip__foot { position: absolute; left: 10px; top: 170px; font-size: 14px; color: var(--text); }
  .small-btn { position: absolute; height: 30px; border: 1px solid var(--btn-line); background: var(--btn-bg); border-radius: 2px; font-size: 12px; font-weight: 700; color: var(--body); text-align: center; line-height: 28px; }
  .event-tile { position: absolute; left: 300px; top: 42px; width: 210px; height: 216px; border: 1px solid var(--line); }
  .event-tile__photo { position: absolute; left: 0; top: 0; width: 100%; height: 160px; background: radial-gradient(ellipse 70px 90px at 90px 80px, #6c7a8c, #2a3546 70%, #17202c); }
  .next-arrow { position: absolute; left: 173px; top: 52px; width: 26px; height: 32px; background: var(--white); border: 1px solid var(--line); border-radius: 2px 0 0 2px; }
  .event-tile__month { position: absolute; left: 14px; top: 173px; font-size: 11px; color: var(--event-red); }
  .event-tile__day { position: absolute; left: 21px; top: 186px; font-size: 18px; color: var(--text); }
  .event-tile__name { position: absolute; left: 55px; top: 171px; font-size: 14px; font-weight: 700; color: var(--link); white-space: nowrap; }
  .event-tile__meta { position: absolute; left: 55px; top: 189px; font-size: 12px; color: var(--muted); white-space: nowrap; }

  .composer { left: 283px; top: 735px; width: 501px; height: 108px; }
  .composer__tabs { position: absolute; left: 0; top: 0; width: 100%; height: 33px; background: var(--btn-bg); border-bottom: 1px solid var(--line); }
  .composer__tab { position: absolute; top: 10px; display: flex; align-items: center; gap: 5px; font-size: 12px; font-weight: 700; }
  .composer__mini { position: absolute; left: 450px; top: 8px; width: 16px; height: 16px; background: #9a6a52; }
  .composer__avatar { position: absolute; left: 11px; top: 45px; width: 40px; height: 40px; background: linear-gradient(135deg, #c89878, #6a4a3a); }
  .composer__prompt { position: absolute; left: 63px; top: 58px; font-size: 14px; color: var(--muted); }

  .shop { left: 283px; top: 855px; width: 501px; height: 100px; }
  .shop__item { position: absolute; top: 39px; width: 149px; height: 60px; }

  .side-box { left: 795px; width: 308px; }
  .info-row { position: absolute; left: 12px; display: flex; align-items: center; gap: 10px; font-size: 12px; color: var(--text); white-space: nowrap; }
  .info-row svg { flex: none; }
  .info-row .strong-link { color: var(--link); font-weight: 700; }
  .info-row .link { color: var(--link); }
  .see-all { position: absolute; right: 12px; top: 8px; font-size: 12px; color: var(--link); }
  .divider { position: absolute; left: 0; width: 100%; height: 1px; background: var(--line); }
  .suggest__pic { position: absolute; left: 12px; width: 52px; height: 52px; }
  .suggest__name { position: absolute; left: 74px; font-size: 14px; font-weight: 700; display: flex; align-items: center; gap: 4px; }
  .suggest__type { position: absolute; left: 74px; font-size: 12px; color: var(--muted); }
  .like-btn { position: absolute; left: 234px; width: 62px; height: 24px; border: 1px solid var(--btn-line); background: var(--btn-bg); border-radius: 2px; font-size: 12px; font-weight: 700; color: var(--body); display: flex; align-items: center; justify-content: center; gap: 4px; }
  .verified { width: 11px; height: 11px; border-radius: 50%; background: #4080ff; display: inline-block; }
</style>
</head>
<body>
  <div class="page"></div>

  <header class="topbar">
    <span class="topbar__brand">Kith</span>
    <div class="topbar__search"></div>
    <div class="topbar__search-btn"></div>
    <svg style="left:475px;top:13px" width="14" height="14" viewBox="0 0 14 14" aria-hidden="true"><circle cx="5.5" cy="5.5" r="4.3" fill="none" stroke="#4b4f56" stroke-width="1.8"/><line x1="8.7" y1="8.7" x2="13" y2="13" stroke="#4b4f56" stroke-width="2"/></svg>
    <div class="topbar__divider" style="left:798px"></div>
    <span class="topbar__home">Home</span>
    <div class="topbar__divider" style="left:856px"></div>
    <svg style="left:873px;top:11px" width="24" height="20" viewBox="0 0 24 20" aria-hidden="true"><g fill="#1d2a4a"><circle cx="8" cy="6" r="4"/><path d="M0 19c0-5 3.5-7.5 8-7.5s8 2.5 8 7.5z"/><circle cx="17" cy="5" r="3.4"/><path d="M15 11c4 0 8 1.5 8 7h-5c0-3-1-5.5-3-7z"/></g></svg>
    <svg style="left:910px;top:11px" width="20" height="20" viewBox="0 0 20 20" aria-hidden="true"><path d="M10 1C5 1 1 4.6 1 9c0 2.4 1.2 4.5 3 6v4l3.5-2c.8.2 1.6.3 2.5.3 5 0 9-3.6 9-8.3S15 1 10 1z" fill="#1d2a4a"/></svg>
    <svg style="left:942px;top:11px" width="20" height="20" viewBox="0 0 20 20" aria-hidden="true"><circle cx="10" cy="10" r="9" fill="#1d2a4a"/><path d="M4 7c2 0 3 1 3 3s2 2 2 4M12 3c0 2 1 3 3 3M11 17c0-2 1-3 3-3" fill="none" stroke="#3b5998" stroke-width="1.6"/></svg>
    <div class="topbar__divider" style="left:979px"></div>
    <svg style="left:993px;top:10px" width="21" height="21" viewBox="0 0 21 21" aria-hidden="true"><circle cx="10.5" cy="10.5" r="10" fill="#1d2a4a"/><text x="10.5" y="15.5" text-anchor="middle" font-family="Arimo, Arial, sans-serif" font-weight="700" font-size="14" fill="#3b5998">?</text></svg>
    <svg style="left:1028px;top:17px" width="11" height="7" viewBox="0 0 11 7" aria-hidden="true"><path d="M0 0h11L5.5 7z" fill="#1d2a4a"/></svg>
  </header>

  <!-- left column -->
  <div class="profile-pic"><div class="profile-pic__art" role="img" aria-label="Album cover artwork: the singer lying in deep blue water, album title beneath"></div></div>
  <h1 class="profile-name">Clara Joy Halden</h1>
  <p class="profile-handle">@clarajoyhaldenmusic</p>
  <ul class="side-nav">
    <li class="is-active">Home</li>
    <li>Tour Dates</li>
    <li>About</li>
    <li>Shop</li>
    <li>Photos</li>
    <li>Likes</li>
    <li>Events</li>
    <li>Videos</li>
    <li>Posts</li>
    <li>Join Mailing List for Clara</li>
  </ul>
  <div class="create-page">Create a Page</div>

  <!-- cover banner -->
  <section class="cover">
    <div class="cover__photo" role="img" aria-label="Misty wintry portrait of the singer in a silver-beaded headdress, teal and grey tones"></div>
    <svg class="cover__frame" width="820" height="311" viewBox="0 0 820 311" aria-hidden="true">
      <g fill="none" stroke="rgba(242,241,235,0.9)" stroke-width="1.2">
        <polyline points="121,16 9,16 9,304 811,304 811,16 407,16"/>
        <polyline points="121,20 13,20 13,300 807,300 807,20 407,20"/>
      </g>
    </svg>
    <h2 class="cover__col cover__title">Clara Joy Halden</h2>
    <p class="cover__col cover__subtitle">LANTERN WALTZ</p>
    <p class="cover__col cover__season">Autumn / Winter tour</p>
    <ul class="cover__col tour-dates">
      <li><span class="date">3<sup>rd</sup> September</span><span class="city">Ravensby</span><span class="venue">Folk Festival</span></li>
      <li><span class="date">21<sup>st</sup> September</span><span class="city">Swindon</span><span class="venue">Calder Theatre</span></li>
      <li><span class="date">1<sup>st</sup> October</span><span class="city">Hitchin</span><span class="venue">Brackwell Folk Club</span></li>
      <li><span class="date">17<sup>th</sup> October</span><span class="city">Bath</span><span class="venue">The Anvil</span></li>
      <li><span class="date">20<sup>th</sup> October</span><span class="city">Sheffield</span><span class="venue">Upper Dale Croquet Club</span></li>
      <li><span class="date">24<sup>th</sup> October</span><span class="city">Birmingham</span><span class="venue">Orchard Lamp Cafe</span></li>
      <li><span class="date">26<sup>th</sup> October</span><span class="city">Glasgow</span><span class="venue">The Nook and Jar</span></li>
      <li><span class="date">27<sup>th</sup> October</span><span class="city">Edinburgh</span><span class="venue">The Marble Parlour</span></li>
      <li><span class="date">8<sup>th</sup> November</span><span class="city">Capital Reel &amp; Ballad Festival</span><span class="venue">The Crooked Heron</span></li>
      <li><span class="date">25<sup>th</sup> November</span><span class="city">Lewes</span><span class="venue">Tandem Record Shop (Live In Store)</span></li>
      <li><span class="date">2<sup>nd</sup> December</span><span class="city">Cambridge</span><span class="venue">The Quayside</span></li>
      <li><span class="date">27<sup>th</sup> January</span><span class="city">Lincolnshire</span><span class="venue">Fenmarsh Theatre</span></li>
    </ul>
    <p class="cover__col cover__tickets">TICKETS/INFO:<span class="url">www.clarajoyhalden-music.example/gigs</span></p>
    <p class="review review__quote" style="right:31px;top:199px">“Rich and expressive”</p>
    <p class="review review__source" style="right:38px;top:226px">BDM MAGAZINE</p>
    <p class="review review__quote" style="right:31px;top:248px">“Vibrant and experimental”</p>
    <p class="review review__source" style="right:38px;top:275px">TUNEPATHS</p>
  </section>

  <!-- action bar -->
  <div class="actions">
    <div class="btn-group">
      <span><svg width="12" height="12" viewBox="0 0 12 12" aria-hidden="true"><path d="M0 5h2.5v7H0zM3.5 5l3-5c1 0 1.5.7 1.3 1.8L7.3 4H11c.7 0 1.1.6 1 1.2l-1 5.6c-.1.7-.6 1.2-1.3 1.2H3.5z" fill="#606770"/></svg>Like</span>
      <span><svg width="12" height="12" viewBox="0 0 12 12" aria-hidden="true"><g fill="none" stroke="#606770" stroke-width="1.6"><path d="M1 1.5a9.5 9.5 0 0 1 9.5 9.5"/><path d="M1 5.5a5.5 5.5 0 0 1 5.5 5.5"/></g><circle cx="2" cy="10" r="1.5" fill="#606770"/></svg>Follow</span>
      <span><svg width="13" height="11" viewBox="0 0 13 11" aria-hidden="true"><path d="M8 0l5 4.8L8 9.6V6.8C4.5 6.8 2 7.8 0 11c.6-4.6 3.4-7.4 8-8z" fill="#606770"/></svg>Share</span>
      <span><svg width="14" height="4" viewBox="0 0 14 4" aria-hidden="true"><g fill="#606770"><circle cx="2" cy="2" r="1.5"/><circle cx="7" cy="2" r="1.5"/><circle cx="12" cy="2" r="1.5"/></g></svg></span>
    </div>
    <div class="send-btn">Send Message</div>
  </div>

  <!-- featured -->
  <section class="card featured">
    <h3 class="card__title" style="top:12px">Featured for you</h3>
    <div class="close-box" style="left:472px;top:11px"><svg width="15" height="15" viewBox="0 0 15 15" aria-hidden="true"><path d="M4 4l7 7M11 4l-7 7" stroke="#fff" stroke-width="1.8"/></svg></div>
    <div class="review-clip">
      <div class="review-clip__text">
        <p>great things about that night, it was with no small degree of anticipation that I pressed play on <i>Lantern Waltz</i>, the debut album from this young songstress. I was not to be disappointed.</p>
        <p>Right from the album opener, ‘Hollin Gate’, it’s easy to see why the leading lights of the folk scene (such as Tom Fairley, Ruth Calloway, Ned Marsh, Jonas Preen to name a few) have been so keen to collaborate with Clara. Her voice is an incredible instrument – distinctive, powerful and timeless, yet wielded with the maturity of a seasoned artist way beyond her years.</p>
      </div>
      <div class="close-box" style="left:259px;top:12px;background:#d4d6da"><svg width="15" height="15" viewBox="0 0 15 15" aria-hidden="true"><path d="M4 4l7 7M11 4l-7 7" stroke="#fff" stroke-width="1.8"/></svg></div>
      <p class="review-clip__foot">100% response rate</p>
      <div class="small-btn" style="left:184px;top:172px;width:88px">Message</div>
    </div>
    <div class="event-tile">
      <div class="event-tile__photo" role="img" aria-label="Portrait of the singer in a beaded headdress against a dark blue backdrop"></div>
      <div class="next-arrow"><svg width="24" height="30" viewBox="0 0 24 30" aria-hidden="true"><path d="M9 9l6 6-6 6" fill="none" stroke="#4b4f56" stroke-width="2.2"/></svg></div>
      <span class="event-tile__month">NOV</span>
      <span class="event-tile__day">8</span>
      <span class="event-tile__name">Clara Joy Halden + F</span>
      <span class="event-tile__meta">Wed 19:30 · The Crooked</span>
    </div>
  </section>

  <!-- composer -->
  <section class="card composer">
    <div class="composer__tabs">
      <span class="composer__tab" style="left:16px"><svg width="13" height="13" viewBox="0 0 13 13" aria-hidden="true"><path d="M0 13l1-4 8-8 3 3-8 8z" fill="#8b6ad3"/></svg>Status</span>
      <span class="composer__tab" style="left:84px;color:var(--link)"><svg width="15" height="13" viewBox="0 0 15 13" aria-hidden="true"><rect x="0" y="2" width="15" height="11" rx="1.5" fill="#7a8294"/><circle cx="7.5" cy="7.5" r="3" fill="#f6f7f9"/></svg>Photo/Video</span>
      <div class="composer__mini" role="img" aria-label="Small page avatar"></div>
      <svg style="position:absolute;left:470px;top:13px" width="9" height="6" viewBox="0 0 9 6" aria-hidden="true"><path d="M0 0h9L4.5 6z" fill="#606770"/></svg>
    </div>
    <div class="composer__avatar" role="img" aria-label="Page avatar photo"></div>
    <p class="composer__prompt">Write something on this Page...</p>
  </section>

  <!-- shop -->
  <section class="card shop">
    <h3 class="card__title" style="top:12px">Shop</h3>
    <div class="shop__item" style="left:16px;background:linear-gradient(180deg,#16243a,#2b4a6e)" role="img" aria-label="Album product cover in deep blue"></div>
    <div class="shop__item" style="left:174px;background:linear-gradient(180deg,#34527a,#7d98b6)" role="img" aria-label="Earlier record product cover in pale blue"></div>
  </section>

  <!-- right column -->
  <section class="card side-box" style="top:455px;height:43px">
    <p class="info-row" style="top:13px;font-size:14px">Musician/band</p>
  </section>

  <section class="card side-box" style="top:511px;height:111px">
    <h3 class="card__label" style="top:8px">Community</h3>
    <p class="info-row" style="top:32px"><svg width="14" height="12" viewBox="0 0 14 12" aria-hidden="true"><g fill="#90949c"><circle cx="5" cy="3.5" r="2.6"/><path d="M0 12c0-3.3 2.2-5 5-5s5 1.7 5 5z"/><circle cx="10.5" cy="3" r="2"/><path d="M9.5 7c2.5 0 4.5 1.2 4.5 4.5h-3c0-2-.5-3.3-1.5-4.5z"/></g></svg><span><span class="strong-link" style="font-weight:400">Invite your friends</span> to like this Page</span></p>
    <p class="info-row" style="top:60px"><svg width="14" height="12" viewBox="0 0 12 12" aria-hidden="true"><path d="M0 5h2.5v7H0zM3.5 5l3-5c1 0 1.5.7 1.3 1.8L7.3 4H11c.7 0 1.1.6 1 1.2l-1 5.6c-.1.7-.6 1.2-1.3 1.2H3.5z" fill="#90949c"/></svg>1,169 people like this</p>
    <p class="info-row" style="top:88px"><svg width="14" height="12" viewBox="0 0 12 12" aria-hidden="true"><g fill="none" stroke="#90949c" stroke-width="1.6"><path d="M1 1.5a9.5 9.5 0 0 1 9.5 9.5"/><path d="M1 5.5a5.5 5.5 0 0 1 5.5 5.5"/></g><circle cx="2" cy="10" r="1.5" fill="#90949c"/></svg>1,161 people follow this</p>
  </section>

  <section class="card side-box" style="top:636px;height:113px">
    <h3 class="card__label" style="top:8px">About</h3>
    <span class="see-all">See All</span>
    <p class="info-row" style="top:33px"><svg width="14" height="14" viewBox="0 0 20 20" aria-hidden="true"><path d="M10 1C5 1 1 4.6 1 9c0 2.4 1.2 4.5 3 6v4l3.5-2c.8.2 1.6.3 2.5.3 5 0 9-3.6 9-8.3S15 1 10 1z" fill="#90949c"/></svg><span class="strong-link">Send message</span></p>
    <p class="info-row" style="top:61px"><svg width="14" height="14" viewBox="0 0 14 14" aria-hidden="true"><g fill="none" stroke="#90949c" stroke-width="1.2"><circle cx="7" cy="7" r="6"/><ellipse cx="7" cy="7" rx="2.6" ry="6"/><line x1="1" y1="7" x2="13" y2="7"/></g></svg><span class="link">tideclip.example/clarajoyhalden</span></p>
    <p class="info-row" style="top:89px"><svg width="14" height="14" viewBox="0 0 14 14" aria-hidden="true"><rect x="1" y="3" width="12" height="10" rx="1" fill="#90949c"/><rect x="4" y="0" width="6" height="4" fill="none" stroke="#90949c" stroke-width="1.4"/><circle cx="7" cy="8" r="2" fill="#fff"/></svg><span class="link">Musician/band</span></p>
  </section>

  <section class="card side-box" style="top:762px;height:200px">
    <h3 class="card__label" style="top:12px">People Also Like</h3>
    <div class="divider" style="top:36px"></div>
    <div class="suggest__pic" style="top:49px;background:linear-gradient(135deg,#5a7a8a,#1d2e3a)" role="img" aria-label="Album artwork of a suggested musician"></div>
    <p class="suggest__name" style="top:57px">Mira Castellan</p>
    <p class="suggest__type" style="top:78px">Musician/band</p>
    <div class="like-btn" style="top:63px"><svg width="12" height="12" viewBox="0 0 12 12" aria-hidden="true"><path d="M0 5h2.5v7H0zM3.5 5l3-5c1 0 1.5.7 1.3 1.8L7.3 4H11c.7 0 1.1.6 1 1.2l-1 5.6c-.1.7-.6 1.2-1.3 1.2H3.5z" fill="#606770"/></svg>Like</div>
    <div class="divider" style="top:114px"></div>
    <div class="suggest__pic" style="top:125px;background:linear-gradient(135deg,#e8e4de,#8a7260)" role="img" aria-label="Portrait of a suggested musician"></div>
    <p class="suggest__name" style="top:135px">Nell Ashby <span class="verified"></span></p>
    <p class="suggest__type" style="top:153px">Musician/band</p>
    <div class="like-btn" style="top:140px"><svg width="12" height="12" viewBox="0 0 12 12" aria-hidden="true"><path d="M0 5h2.5v7H0zM3.5 5l3-5c1 0 1.5.7 1.3 1.8L7.3 4H11c.7 0 1.1.6 1 1.2l-1 5.6c-.1.7-.6 1.2-1.3 1.2H3.5z" fill="#606770"/></svg>Like</div>
  </section>

  <!-- page ends above the white margin -->
  <div class="abs" style="left:0;top:938px;width:1200px;height:62px;background:var(--white)"></div>
</body>
</html>
```